New Business Card Design Project

I have a logo I would like to use on the business card. I want something that will stand out and that will be remembered.

Target Market(s)

People who collect gems, minerals and crystals.

Contact Information for Business Card

email - mkthestonefalcon@vendrollo.com
phone # 917-406-2581

Font styles to use
Serif
Sans Serif
Decorative

Colors

Designer to choose colors to be used in the design.

Requirements
Must have
• The logo...two to choose from.
Nice to have
• An eye catching and memorable way to draw in people who collect gems minerals and crystals.

```html
<!DOCTYPE html>
<html lang="en">
<head>
<meta charset="utf-8">
<title>The Stone Falcon – Business Card</title>
<link rel="stylesheet" href="https://fonts.googleapis.com/css2?family=Cinzel:wght@500&family=Lato:wght@400;900&display=swap">
<style>
  :root {
    --backdrop: #d9d9d9;
    --card-dark: #050505;
    --card-light: #ffffff;
    --ink: #111111;
    --accent: #2626c9;
    --muted: #2b2b2b;
    --ghost: #ececee;
    --ghost-edge: #e2e2e6;
  }
  * { box-sizing: border-box; margin: 0; padding: 0; }
  html, body {
    width: 1200px; height: 900px; overflow: hidden;
    background: var(--backdrop);
    font-family: "Lato", Arial, sans-serif;
  }
  .canvas { position: relative; width: 1200px; height: 900px; }
  .card {
    position: absolute; width: 560px; height: 320px;
    border-radius: 26px; overflow: hidden;
    box-shadow: 0 14px 30px rgba(0,0,0,0.22);
  }
  /* back side */
  .card--back {
    left: 60px; top: 110px; background: var(--card-dark);
    display: flex; flex-direction: column; align-items: center; justify-content: center;
    color: #fff;
  }
  .brand-mark { display: flex; align-items: center; gap: 14px; }
  .brand-dot { width: 22px; height: 22px; border-radius: 50%; background: var(--accent); }
  .brand-name {
    font-family: "Lato", Arial, sans-serif; font-weight: 900;
    letter-spacing: 0.02em; text-transform: uppercase;
  }
  .card--back .brand-name { font-size: 38px; color: #fff; }
  .website { margin-top: 26px; font-size: 17px; letter-spacing: 0.02em; color: #fff; }
  /* front side */
  .card--front { left: 580px; top: 470px; background: var(--card-light); }
  .mascot-ghost {
    position: absolute; right: 24px; top: 18px; width: 220px; height: 284px;
    border-radius: 110px 110px 60px 60px;
    background: radial-gradient(circle at 50% 35%, var(--ghost), var(--ghost-edge));
  }
  .front-content { position: absolute; left: 34px; top: 58px; }
  .card--front .brand-name { font-size: 40px; color: var(--ink); line-height: 1; }
  .contact-block { margin-top: 72px; }
  .person-name {
    font-family: "Cinzel", Georgia, serif; font-weight: 500;
    font-size: 23px; color: var(--accent); line-height: 1.1;
  }
  .person-title { font-size: 16px; color: var(--muted); margin-bottom: 10px; }
  .contact-line {
    display: flex; align-items: center; gap: 8px;
    font-size: 16px; color: var(--muted); line-height: 1.45;
  }
  .contact-icon { width: 14px; height: 14px; fill: var(--accent); flex: none; }
</style>
</head>
<body>
<main class="canvas">
  <section class="card card--back" aria-label="Card back">
    <div class="brand-mark">
      <span class="brand-dot"></span>
      <span class="brand-name">The Stone Falcon</span>
    </div>
    <p class="website">www.thestonefalcon.com</p>
  </section>

  <section class="card card--front" aria-label="Card front">
    <div class="mascot-ghost" role="img" aria-label="Faint mascot illustration holding crystals"></div>
    <div class="front-content">
      <div class="brand-name">The Stone Falcon</div>
      <div class="contact-block">
        <p class="person-name">MARTA KELLERMAN</p>
        <p class="person-title">Managing Director</p>
        <p class="contact-line">
          <svg class="contact-icon" viewBox="0 0 16 16" aria-hidden="true"><path d="M3 1h3l1.5 4-2 1.3a9 9 0 0 0 4.2 4.2L11 8.5l4 1.5v3a2 2 0 0 1-2 2A13 13 0 0 1 1 3a2 2 0 0 1 2-2z"/></svg>
          917-406-2581
        </p>
        <p class="contact-line">
          <svg class="contact-icon" viewBox="0 0 16 16" aria-hidden="true"><path d="M1 3h14v10H1z M1 3l7 6 7-6" stroke="#fff" stroke-width="1.2"/></svg>
          mkthestonefalcon@vendrollo.com
        </p>
      </div>
    </div>
  </section>
</main>
</body>
</html>
```